Flyer-Design für Unternehmensberatung
Zielgruppe
Unternehmensberatung und biete Beratung zur Gründung, Marketing, Kundengewinnung und Kooperation. Meine Zielgruppe sind Heilpraktikerinnen und Heilpraktiker für Psychotherapie, die Ihre Praxis gründen, meist ab 45 Jahre.
Aufgabenstellung
Der Flyer soll in einen Umschlag von 22 x 11 cm passen. Die Farben vom Logo bitte berücksichtigen.

```html
<!DOCTYPE html>
<html lang="de">
<head>
<meta charset="utf-8">
<title>Flyer – Brandt Organisation</title>
<link href="https://fonts.googleapis.com/css2?family=Montserrat:wght@800&family=Encode+Sans+Semi+Condensed:wght@300;400&display=swap" rel="stylesheet">
<style>
  :root{
    --red-deep:#b8180c;
    --red-mid:#d8300f;
    --red-light:#ec5a1c;
    --stripe-red:#d4131a;
    --slate:#58585a;
    --white:#ffffff;
    --photo-warm:#e9b99a;
    --photo-cool:#cfd6dc;
  }
  *{box-sizing:border-box;margin:0;padding:0}
  html,body{width:849px;height:1200px;overflow:hidden;background:var(--white)}
  body{position:relative;font-family:"Encode Sans Semi Condensed",sans-serif;color:var(--white)}
  .sheet{position:absolute;left:20px;width:808px;height:570px;overflow:hidden;
    background:radial-gradient(ellipse at 55% 45%,var(--red-light) 0%,var(--red-mid) 45%,var(--red-deep) 100%)}
  .sheet--outside{top:25px}
  .sheet--inside{top:614px}
  .panel{position:absolute;top:0;height:570px;width:269px}
  .panel--bio{left:0}
  .panel--contact{left:269px;border-left:1px solid rgba(255,255,255,.25);border-right:1px solid rgba(255,255,255,.25)}
  .panel--cover{left:539px;width:269px}
  .photo{position:absolute}
  .photo--portrait{left:0;top:0;width:269px;height:215px;background:linear-gradient(135deg,var(--photo-cool),var(--photo-warm) 60%,#f4f1ec)}
  .photo--cover{left:0;top:0;width:269px;height:445px;background:linear-gradient(180deg,rgba(0,0,0,0) 0%,rgba(40,10,5,.25) 60%,rgba(20,10,10,.45) 100%)}
  .accent{position:absolute;left:0;top:131px}
  h2{font-family:"Montserrat",sans-serif;font-weight:800;font-size:14.5px;letter-spacing:.2px}
  .bio-title{position:absolute;left:19px;top:295px}
  .bio-text{position:absolute;left:21px;top:318px;width:240px;font-size:8.6px;line-height:11.4px;font-weight:300}
  .bio-text p+p{margin-top:11px}
  .contact-title{position:absolute;top:295px;width:100%;text-align:center}
  .contact-list{position:absolute;top:318px;width:100%;text-align:center;list-style:none;font-size:9.4px;line-height:16.9px;font-weight:300}
  .brand-box{position:absolute;left:0;bottom:0;width:100%;height:125px;background:var(--white);
    display:flex;align-items:center;justify-content:center;gap:10px;color:var(--red-deep)}
  .brand-mark{width:16px;height:16px;background:var(--stripe-red)}
  .brand-name{font-family:"Encode Sans Semi Condensed",sans-serif;font-weight:400;font-size:14px;line-height:16px;color:var(--slate)}
  .cover-title{position:absolute;left:19px;top:448px;font-family:"Montserrat",sans-serif;font-weight:800;font-size:29px;line-height:37px;letter-spacing:.3px}
  .inside-art{position:absolute;inset:0}
  .intro{position:absolute;left:21px;top:19px;width:250px;font-size:11.2px;line-height:14px;font-weight:300}
  .intro p+p{margin-top:13px}
  .intro strong,.case strong{font-family:"Montserrat",sans-serif;font-weight:800;font-size:10.4px}
  .case{position:absolute;font-size:10.4px;line-height:13.8px;font-weight:300}
  .case p+p{margin-top:5px}
  .case--left{left:288px;top:210px;width:236px}
  .case--right{left:557px;top:373px;width:238px}
  .case strong{font-size:10px}
</style>
</head>
<body>
  <section class="sheet sheet--outside">
    <div class="panel panel--bio">
      <div class="photo photo--portrait" role="img" aria-label="Porträtfoto der Beraterin"></div>
      <svg class="accent" width="90" height="90" viewBox="0 0 90 90" aria-hidden="true">
        <polygon points="0,0 0,10 62,84 72,84" fill="var(--slate)"/>
        <polygon points="0,18 0,26 48,84 57,84" fill="var(--stripe-red)"/>
      </svg>
      <h2 class="bio-title">HEIKE BRANDT</h2>
      <div class="bio-text">
        <p>Ihr Erfahrungsspektrum liegt in der ganzheitlichen Beratung von Selbstständigen von der Idee, über die Angebotserstellung und das Marketing, bis zum ersten Kunden. Ihre beruflichen Wurzeln liegen in medizinischen Bereichen und als Beraterin im Qualitätsmanagement von Industrieunternehmen. Ihre Unternehmensberatung gründet sie in 2011. Sie steigt nach dem wirtschaftswissenschaftlichen Studium als Beraterin ein.</p>
        <p>Mit Ihrem umfassenden Wissen und Kenntnisstand gelingt Ihr die ganzheitliche Sicht auf Kleinunternehmen und Praxen, auch bei Beginn einer Selbstständigkeit. Viele positive Rückmeldungen Ihrer Kunden bestärken sie weiterhin auf dem Fachgebiet zu beraten.</p>
        <p>Als ehemalige Vizepräsidentin in einem Wirtschaftsverband begleitete sie einige Jahre die Unternehmer und Selbstständigen mit Wissen, Themen und Vorträgen rund um die Selbstständigkeit, Gründung und Kooperation.</p>
      </div>
    </div>

    <div class="panel panel--contact">
      <h2 class="contact-title">KONTAKT</h2>
      <ul class="contact-list">
        <li>Heike Brandt, Diplom-Kauffrau</li>
        <li>Am Feldrain 8/2</li>
        <li>71299 Lindenau</li>
        <li>Telefon 07031 48207</li>
        <li>Mobil 0152 40318275</li>
        <li>info@brandt-organisation.de</li>
        <li>www.brandt-organisation.de</li>
      </ul>
      <div class="brand-box">
        <span class="brand-mark"></span>
        <span class="brand-name">BRANDT<br>ORGANISATION</span>
      </div>
    </div>

    <div class="panel panel--cover">
      <div class="photo photo--cover" role="img" aria-label="Foto einer begeisterten jungen Frau mit Smartphone"></div>
      <h1 class="cover-title">PATIENTEN MIT<br>LEICHTIGKEIT<br>GEWINNEN</h1>
    </div>
  </section>

  <section class="sheet sheet--inside">
    <svg class="inside-art" width="808" height="570" viewBox="0 0 808 570">
      <polygon points="438,0 808,0 808,286 757,323" fill="var(--slate)"/>
      <polygon points="401,0 424,0 752,330 735,330" fill="var(--stripe-red)"/>
      <defs>
        <linearGradient id="sunset" x1="0" y1="0" x2="1" y2="1">
          <stop offset="0" stop-color="#7a3a2a"/>
          <stop offset=".55" stop-color="#f2a24a"/>
          <stop offset="1" stop-color="#e8692a"/>
        </linearGradient>
        <linearGradient id="handshake" x1="0" y1="0" x2="1" y2="1">
          <stop offset="0" stop-color="#e7ecf2"/>
          <stop offset=".6" stop-color="#b9cbe2"/>
          <stop offset="1" stop-color="#7d98c0"/>
        </linearGradient>
      </defs>
      <polygon points="609,2 808,2 808,245 757,311 552,106" fill="url(#sunset)" role="img" aria-label="Foto einer jubelnden Person vor Sonnenuntergang"/>
      <polygon points="0,209 262,474 151,570 0,570" fill="var(--slate)"/>
      <polygon points="106,274 118,274 268,430 262,440" fill="var(--stripe-red)"/>
      <polygon points="0,303 262,474 151,570 0,570" fill="url(#handshake)" role="img" aria-label="Foto eines älteren Paares beim Händeschütteln"/>
    </svg>

    <div class="intro">
      <p>Ihre Praxisräume sind eingerichtet und keiner ruft Sie an. Vergeblich hoffen Sie auf neue Patienten. Nach zwei Tagen die ersten Patienten gewinnen und somit kontinuierlich Patienten gewinnen. Sie als praktizierende Heilpraktikerin planen das auch?</p>
      <p>Mein erweitertes Intensiv-Angebot sind 2 x 2 Stunden Marketing- und Kooperationsberatung: Analyse, Beratung und Optimierung.</p>
      <p><strong>Sie erfahren in einem kostenfreien Erstgespräch was möglich ist. Vereinbaren Sie einen Termin!</strong></p>
    </div>

    <div class="case case--left">
      <p><strong>Erfolgreich abgeschlossene Projekte im Gesundheitsbereich:</strong></p>
      <p>Patientengewinnung und Aufbau der eigenen Selbstständigkeit im Gesundheitsbereich</p>
      <p><strong>Die Aufträge:</strong> Marketing für den Praxisaufbau nach Gründung</p>
      <p>Beratungsumfang: 4 Stunden</p>
      <p><strong>Ausgangslage:</strong> Die Praxisräume waren vorhanden. Noch keine Patienten in der Praxis, kein Flyer, keine Webseite, keine Visitenkarte vorhanden.</p>
      <p><strong>Ziele meiner Kundinnen:</strong> Patienten für die Privat-Praxis gewinnen und auffinden geeigneter Kooperationspartner</p>
    </div>

    <div class="case case--right">
      <p>Maßnahmen zur Patientengewinnung festgelegt, Spezialisierung, Text und Bildervorschläge für ersten Flyer und Visitenkarten. Themen für die Webseite erarbeitet. Maßnahmen festgelegt, um Kooperationspartner zu gewinnen, Inhalte für eigene Webseite festgelegt, Plattformen für Veröffentlichung.</p>
      <p><strong>Ergebnisse bei Kundinnen:</strong> nach 2 Tagen, die ersten Patienten gewonnen und heute kontinuierliche Patientengewinnung.</p>
      <p><strong>Interessiert?<br>Rufen Sie mich an: 07031 48207</strong></p>
    </div>
  </section>
</body>
</html>
```